Global Expert Network Firm needs business card design

We need business card design for a new company based in Seoul, South Korea called 'Corwell Insight Partners'. We recruit industry experts covering all countries and connect our client and recruited expert by phone, face-to-face meetings and etc. We are a global expert network firm that is focused on delivering high-quality experts to our clients throughout the world. Our clients include multinational corporations, global consulting firms, private equity firms, venture capital firms, asset management companies.
We have made new logo and please find attachment.(Please use new logo)
Target Market(s)
Global Consulting Firms, Investment Firms, Private Equity Firms, Venture Capital Firms.
Industry/Entity Type
Recruitment
Contact Information for Business Card
We need two Languages (English and Korean Version).
The front is Korean and the back is English version.
[The back] [English]
Company Name: Corwell Insight Partners, Inc.
CEO Name: Daniel Park
Address: #507, Hanbit Bldg, 82 Maebongsan-ro, Dobong-gu, Seoul, 01327, Korea
Tel. +82 2 718 4052
Fax. +82 2 864 1097
Mobile. +82 10 7264 8815
Email: daniel@corwellip.com
Web: www.corwellip.com
[The front] [Korean] => Described in same order as English version.
회사명: 코웰인사이트파트너스(주)
대표이사: 박도현
주소: 서울시 도봉구 매봉산로 82 한빛빌딩 507호
Tel. 02 718 4052
Fax. 02 864 1097
Mobile. 010 7264 8815
Web: www.corwellip.com
Look and feel
Each slider illustrates characteristics of the customer's brand and the style your logo design should communicate.

```html
<!DOCTYPE html>
<html lang="en">
<head>
<meta charset="utf-8">
<title>Corwell Insight Partners — Business Card</title>
<link rel="stylesheet" href="https://fonts.googleapis.com/css2?family=Arimo:wght@700&family=Open+Sans:wght@400;700&display=swap">
<style>
  :root {
    --card-bg: #111113;
    --band-top: rgba(17, 17, 19, 0);
    --band-blue: #2d3f9e;
    --band-blue-deep: #26368c;
    --ink: #ffffff;
  }
  * { margin: 0; padding: 0; box-sizing: border-box; }
  html, body {
    width: 1200px;
    height: 686px;
    overflow: hidden;
    background: var(--card-bg);
  }
  .card {
    position: relative;
    width: 1200px;
    height: 686px;
    background: var(--card-bg);
    color: var(--ink);
    font-family: "Open Sans", Arial, sans-serif;
    overflow: hidden;
  }
  .band {
    position: absolute;
    bottom: 0;
    background: linear-gradient(to bottom, var(--band-top) 0%, var(--band-blue-deep) 35%, var(--band-blue) 100%);
  }
  .band--left  { left: 32px;   width: 41px;  top: 110px; }
  .band--mid   { left: 935px;  width: 82px;  top: 215px; }
  .band--right { left: 1043px; width: 117px; top: 45px; }

  .brand-name {
    position: absolute;
    left: 84px;
    top: 200px;
    font-family: "Open Sans", Arial, sans-serif;
    font-weight: 400;
    font-size: 30px;
    line-height: 1;
    white-space: nowrap;
    color: var(--ink);
  }

  .person {
    position: absolute;
    right: 117px;
    top: 70px;
    font-family: "Arimo", Arial, sans-serif;
    font-weight: 700;
    font-size: 50px;
    line-height: 1;
  }
  .company {
    position: absolute;
    right: 86px;
    top: 256px;
    font-family: "Arimo", Arial, sans-serif;
    font-weight: 700;
    font-size: 37px;
    line-height: 1;
  }
  .label { font-weight: 700; }
  .gap { display: inline-block; width: 22px; }
  .contact {
    position: absolute;
    right: 94px;
    top: 345px;
    text-align: right;
    font-size: 35px;
    line-height: 51px;
    white-space: nowrap;
  }
  .address {
    position: absolute;
    right: 94px;
    top: 451px;
    text-align: right;
    font-style: normal;
    font-size: 30px;
    line-height: 45px;
    white-space: nowrap;
  }
  .web-row {
    position: absolute;
    right: 94px;
    top: 596px;
    font-size: 37px;
    line-height: 1.2;
    white-space: nowrap;
  }
</style>
</head>
<body>
<main class="card">
  <div class="band band--left"></div>
  <div class="band band--mid"></div>
  <div class="band band--right"></div>

  <p class="brand-name">Corwell Insight Partners</p>

  <h1 class="person">Daniel Park</h1>
  <h2 class="company">Corwell Insight Partners, Inc.</h2>

  <div class="contact">
    <p><span class="label">Fax.</span> 02 864 1097</p>
    <p><span class="label">Tel.</span> 02 718 4052<span class="gap"></span><span class="label">Mobile.</span> 010 7264 8815</p>
  </div>

  <address class="address">
    <p><span class="label">Address:</span> #507, Hanbit Bldg,</p>
    <p>82 Maebongsan-ro, Dobong-gu,</p>
    <p>Seoul, 01327, Korea</p>
  </address>

  <p class="web-row"><span class="label">Email:</span> daniel@corwellip.com<span class="gap"></span><span class="label">Web:</span> www.corwellip.com</p>
</main>
</body>
</html>
```